Speakwell election of Region 17 Club Growth Director.

This is a tri-fold brochure. I have a basic layout from last years election but would like to add some detail and punch to the campaign brochure. I have a sample from last year. I've also included a sample of a brochure with some depth and personality. The design should communicate that I am a transformational leader who has a solid foundation in helping others to build a better Speakwell experience. If you have the winning design I will need business cards, post cards, and a poster.

Target Market(s)

Speakwell leaders with in Georgia. 25 yrs to 64 yrs = 80% of membership; 51% are female, over 75% have at least a Bachelor's degree or higher; 40% are specialist and 24% managers; 27% earn $100,000 or more - 41% earn $75,000 per year.

Industry/Entity Type

Non-Profit

Font styles to use
Sans Serif

Requirements
Must have
• Professional look. Playing off my experience as a residential contractor. Nickname is "steel toe" Dorwick.
Nice to have
• larger font
Should not have
• Can not be hard to read

```html
<!DOCTYPE html>
<html lang="en">
<head>
<meta charset="utf-8">
<title>Speakwell Region 17 – Campaign Brochure</title>
<link href="https://fonts.googleapis.com/css2?family=Bebas+Neue&family=Fira+Sans:wght@400;500&display=swap" rel="stylesheet">
<style>
  :root {
    --stage: #fdf25a;
    --hazard: #f7d31b;
    --hazard-deep: #e2c21c;
    --ink: #111111;
    --night: #1b1b1b;
    --night-glow: #4a4a4a;
    --concrete-light: #e4e4e4;
    --concrete: #c9c9c9;
    --concrete-dark: #a9a9a9;
    --paper: #f4f4f4;
    --fold: #1a1a1a;
  }
  * { box-sizing: border-box; margin: 0; padding: 0; }
  html, body { width: 1200px; height: 940px; overflow: hidden; }
  body {
    background: var(--stage);
    position: relative;
    font-family: "Fira Sans", Arial, sans-serif;
  }
  .fold-line {
    position: absolute; top: 24px; width: 1px; height: 892px;
    background: var(--fold);
  }
  .fold-line--one { left: 420px; }
  .fold-line--two { left: 768px; }

  .brochure {
    position: absolute; left: 72px; top: 102px;
    width: 1046px; height: 740px;
    display: flex;
    box-shadow: 8px 10px 10px rgba(0,0,0,0.35);
  }

  /* ---------- shared ---------- */
  .banner {
    position: absolute;
    font-family: "Bebas Neue", Impact, sans-serif;
    font-weight: 400;
    color: var(--ink);
    font-size: 31px;
    line-height: 1;
    letter-spacing: -0.3px;
    white-space: nowrap;
    display: flex; align-items: center;
    z-index: 1;
  }
  .banner::before {
    content: ""; position: absolute; inset: 0; z-index: -1;
    background: var(--hazard);
    clip-path: polygon(0 6%, 100% 0, 89% 100%, 0 100%);
  }
  .hazard-stripes { position: absolute; left: 0; bottom: 0; }

  /* ---------- cover panel ---------- */
  .cover {
    position: relative; width: 348px; height: 100%; overflow: hidden;
    background:
      radial-gradient(ellipse at 30% 10%, var(--concrete-dark) 0%, transparent 45%),
      radial-gradient(ellipse at 70% 60%, var(--concrete-light) 0%, transparent 60%),
      linear-gradient(160deg, var(--concrete) 0%, var(--concrete-light) 55%, var(--concrete) 100%);
  }
  .cover .banner { left: 0; top: 56px; width: 302px; height: 43px; padding-left: 38px; }
  .cover-copy, .cover-aside {
    position: absolute;
    font-size: 13.5px; line-height: 16.4px; color: var(--ink);
    text-align: justify; hyphens: auto; font-weight: 400;
  }
  .cover-copy { left: 38px; top: 126px; width: 265px; }
  .cover-copy p + p { margin-top: 16.4px; }
  .cover-aside { left: 150px; top: 306px; width: 153px; z-index: 2; }
  .candidate-photo {
    position: absolute; left: 0; top: 316px; width: 330px; height: 424px;
    background: linear-gradient(170deg, #d9d9d9 0%, #f1f1f1 45%, #e6e6e6 100%);
    clip-path: polygon(10% 0, 45% 0, 55% 45%, 100% 30%, 100% 50%, 80% 100%, 0 100%, 0 25%);
  }

  /* ---------- inside panels ---------- */
  .inside {
    position: relative; flex: 1; height: 100%; overflow: hidden;
    background: radial-gradient(ellipse at 55% 55%, var(--night-glow) 0%, #2a2a2a 40%, var(--night) 75%);
  }
  .inside .banner { left: 0; top: 54px; width: 310px; height: 44px; padding-left: 42px; }

  .award { position: absolute; width: 266px; color: var(--paper); }
  .award-head { display: flex; gap: 21px; align-items: flex-start; margin-bottom: 10px; }
  .award-badge {
    flex: none; width: 72px; height: 72px; padding: 5px;
    background: repeating-linear-gradient(45deg, var(--hazard) 0 6px, var(--ink) 6px 12px);
  }
  .award-badge > * { width: 100%; height: 100%; display: block; }
  .award-title {
    font-family: "Bebas Neue", Impact, sans-serif; font-weight: 400;
    color: var(--hazard); font-size: 24px; line-height: 1;
    letter-spacing: -0.2px;
    margin: 4px 0 6px;
  }
  .award-lead, .award-body { font-size: 11.5px; line-height: 13.4px; }
  .award-lead { width: 178px; }
  .award-body { text-align: justify; hyphens: auto; }

  .fill-wordcloud { background: linear-gradient(135deg, #f2f2f2, #c9d3e4); }
  .fill-portrait { background: linear-gradient(160deg, #8a7a6a, #2a3158 70%); }
  .fill-gavel { background: linear-gradient(135deg, #d6d2cc, #5a3a24 70%); }
  .shape-disc { border-radius: 50%; background: radial-gradient(circle, #d8c98a 0 55%, #2d4d8a 56%); }
  .shape-pin { background: #5e5e5e; display: flex !important; align-items: center; justify-content: center; }
  .shape-pin span { width: 70%; height: 70%; border-radius: 50%; background: #c9a84a; }
  .shape-card { background: linear-gradient(180deg, #2b3f6b 0 55%, #e8e8e8 55%); }
</style>
</head>
<body>
  <div class="fold-line fold-line--one"></div>
  <div class="fold-line fold-line--two"></div>

  <main class="brochure">
    <section class="cover">
      <h1 class="banner">Building a Better Future</h1>
      <div class="cover-copy">
        <p>Quas nominavi appetere sea te. Novum impedit nonumes ne vel, nec at solet aliquam.</p>
        <p>Mundi aliquip scribentur ut vim, cu usu ignota iuvaret honestatis. Et ius argumentum disputando, cum ut electram suscipiantur, an illud decore mel.</p>
        <p>Sed et mucius minimum, quas nostrum ea ius.</p>
      </div>
      <svg class="hazard-stripes" width="348" height="67" viewBox="0 0 348 67" aria-hidden="true">
        <polygon points="0,67 28,67 50,0 0,0" fill="var(--hazard-deep)"/>
        <polygon points="205,67 240,67 262,0 227,0" fill="var(--hazard-deep)"/>
        <polygon points="270,67 320,67 342,0 292,0" fill="var(--hazard-deep)"/>
      </svg>
      <div class="candidate-photo" role="img" aria-label="Photo of the candidate in a white hard hat and white jacket, gesturing toward the text"></div>
      <p class="cover-aside">Ad similique elaboraret pri, mel volutpat liberavisse ex, at duo eleifend postulant incorrupte.</p>
    </section>

    <section class="inside">
      <h2 class="banner">Speakwell of the Year</h2>

      <article class="award" style="left:41px; top:143px;">
        <div class="award-head">
          <div class="award-badge"><div class="fill-wordcloud" role="img" aria-label="Word cloud of leadership and coaching terms"></div></div>
          <div><h3 class="award-title">District Leader</h3><p class="award-lead">Quas nominavi appetere sea te. Novum impedit nonumes ne vel, nec at solet aliquam.</p></div>
        </div>
        <p class="award-body">Quas nominavi appetere sea te. Novum impedit nonumes ne vel, nec at solet aliquam.<br>Mundi aliquip scribentur ut vim, cu usu ignota iuvaret honestatis. Et ius argumentum disputando, cum ut electram suscipiantur, an illud decore mel.<br>Sed et mucius minimum, quas nostrum ea ius.<br>Ad similique elaboraret pri, mel volutpat liberavisse ex, at duo eleifend postulant incorrupte.</p>
      </article>

      <article class="award" style="left:41px; top:378px;">
        <div class="award-head">
          <div class="award-badge"><div class="shape-disc" role="img" aria-label="Conference badge"></div></div>
          <div><h3 class="award-title">Conference Leader</h3><p class="award-lead">Quas nominavi appetere sea te. Novum impedit nonumes ne vel, nec at solet aliquam.</p></div>
        </div>
        <p class="award-body">Quas nominavi appetere sea te. Novum impedit nonumes ne vel, nec at solet aliquam.<br>Mundi aliquip scribentur ut vim, cu usu ignota iuvaret honestatis.</p>
      </article>

      <article class="award" style="left:41px; top:543px;">
        <div class="award-head">
          <div class="award-badge"><div class="shape-pin" role="img" aria-label="Club president pin"><span></span></div></div>
          <div><h3 class="award-title">Club Leader</h3><p class="award-lead">Quas nominavi appetere sea te. Novum impedit nonumes ne vel, nec at solet aliquam.</p></div>
        </div>
        <p class="award-body">Quas nominavi appetere sea te. Novum impedit nonumes ne vel, nec at solet aliquam.</p>
      </article>

      <article class="award" style="left:383px; top:56px;">
        <div class="award-head">
          <div class="award-badge"><div class="shape-card" role="img" aria-label="Outstanding member badge"></div></div>
          <div><h3 class="award-title">Membership</h3><p class="award-lead">Quas nominavi appetere sea te. Novum impedit nonumes ne vel, nec at solet aliquam.</p></div>
        </div>
        <p class="award-body">Quas nominavi appetere sea te. Novum impedit nonumes ne vel, nec at solet aliquam.<br>Mundi aliquip scribentur ut vim, cu usu ignota iuvaret honestatis.<br>Mundi aliquip scribentur ut vim, cu usu ignota iuvaret honestatis.</p>
      </article>

      <article class="award" style="left:383px; top:240px;">
        <div class="award-head">
          <div class="award-badge"><div class="fill-portrait" role="img" aria-label="Photo of the candidate speaking at a lectern"></div></div>
          <div><h3 class="award-title">Speaker</h3><p class="award-lead">Quas nominavi appetere sea te. Novum impedit nonumes ne vel, nec at solet aliquam.</p></div>
        </div>
        <p class="award-body">Quas nominavi appetere sea te. Novum impedit nonumes ne vel, nec at solet aliquam.<br>Mundi aliquip scribentur ut vim, cu usu ignota iuvaret honestatis.</p>
      </article>

      <article class="award" style="left:383px; top:404px;">
        <div class="award-head">
          <div class="award-badge"><div class="fill-gavel" role="img" aria-label="Photo of a judge's gavel"></div></div>
          <div><h3 class="award-title">Chief Judge</h3><p class="award-lead">Quas nominavi appetere sea te. Novum impedit nonumes ne vel, nec at solet aliquam.</p></div>
        </div>
        <p class="award-body">Quas nominavi appetere sea te. Novum impedit nonumes ne vel, nec at solet aliquam.<br>Mundi aliquip scribentur ut vim, cu usu ignota iuvaret honestatis. Et ius argumentum disputando, cum ut electram suscipiantur, an illud decore mel.<br>Sed et mucius minimum, quas nostrum ea ius.<br>Ad similique elaboraret pri, mel volutpat liberavisse ex, at duo eleifend postulant incorrupte.<br>Sed et mucius minimum, quas nostrum ea ius.<br>Ad similique elaboraret pri, mel volutpat liberavisse ex, at duo eleifend postulant incorrupte.</p>
      </article>

      <svg class="hazard-stripes" width="698" height="67" viewBox="0 0 698 67" aria-hidden="true">
        <g fill="var(--hazard-deep)">
          <polygon points="0,67 50,67 70,2 12,0"/>
          <polygon points="80,67 136,67 158,2 102,0"/>
          <polygon points="172,67 228,67 250,2 194,0"/>
          <polygon points="264,67 320,67 342,2 286,0"/>
          <polygon points="356,67 412,67 434,2 378,0"/>
          <polygon points="448,67 504,67 526,2 470,0"/>
          <polygon points="540,67 596,67 618,2 562,0"/>
          <polygon points="632,67 688,67 698,30 698,0 654,0"/>
        </g>
      </svg>
    </section>
  </main>
</body>
</html>
```